Long Island, NY modeling and acting company needs a lead generation landing page

I want the page to look similar as the set up is for www.castingharborview.com but instead of being for San Diego, CA USA this is for Long Island, NY USA.

At the top instead of saying ( San Diego Talent Auditions, Get Started in TV Commercials, Movies, Magazines & More!) I would like it to say ( Long Island Talent Audtions, Get Started in TV Commercials, Movies, Magazines & More! )

Underneath a picture of NY City with either those same pictures (without the Miles Dentry Hallow logo on Trent Vasquell's picture) or another group of pictures with actors and actresses from the shows below.

I would prefer the landing page have pictures of top TV rated shows appealing to families (and kids) like Pip & Tully, Marnie, Rowan & Bea, Surf Camp Caper, Suburb Clan, Beyond the thicket, Gravel under the blue porch, The Hinge, Quark Lab Crew, Quiet Clever Sisters. Also, mixed with print advertising photos that look they are from (or are from) stores like Wex, Morrow, Ferrule, Lumen 46, Thistlewade, Red Pier type print ads.

Hopefully the designer can source images/vdeo's in the public domain.

Underneath the picture at the top I would like it to say: You could be our next Success Story!

I would like Bright colors!!

(This is the copy I would like under the first video at www.castingharborview.com) for this landing page.

Get Started in TV Commercials, Movies, Magazines & More!

Enter today for your chance to be on a show like Marnie, Quiet clever sisters, The Spooky Pembertons and more! We are pre-screening for Hollywood's top Agents and Casting Directors. One lucky winner will win an all expense paid trip to New York City to meet hundreds of top agents, casting directors and managers.

Ages 4 - 30 yrs only

Auditions are being held in the Long Island Area! (map of Long island, with a star?)

This is the copy I would like above the fill in form for the leads.

Have you ever thought about being on TV or in Magazines?

Fill out the form now for your chance to get started today!
You will be contacted for the next available audition you are qualified for.

Additional Ideas - But Maybe too complicated

I would like to add a box for talent to upload a photo

Select: Put a picture-
models Actors performers
maybe one photo in each category,

If designer needs assistance with content I would be glad to help

```html
<!DOCTYPE html>
<html lang="en">
<head>
<meta charset="utf-8">
<title>Bayline Talent Auditions</title>
<link rel="stylesheet" href="https://fonts.googleapis.com/css2?family=Alice&family=Open+Sans:wght@400;600;700&display=swap">
<style>
  :root{
    --teal:#1ba3b5;
    --teal-dark:#0e6e7c;
    --teal-deep:#0a5560;
    --orange:#f7941d;
    --orange-dark:#e07b0a;
    --ink:#222;
    --band:#d6d6d6;
    --card:#ffffff;
    --footer:#3a3a3a;
    --sky-top:#0b1030;
    --sky-mid:#2a2a6a;
    --sky-low:#7a3a6e;
  }
  *{box-sizing:border-box;margin:0;padding:0}
  html,body{width:1200px;height:2568px;overflow:hidden;background:#fff}
  body{font-family:"Open Sans",Arial,sans-serif;color:var(--ink);position:relative}

  .site-header{position:absolute;left:0;top:0;width:1200px;height:110px;text-align:center;background:#fff}
  .site-title{font-family:"Alice",Georgia,serif;color:var(--teal);font-size:46px;font-weight:400;padding-top:10px;letter-spacing:.5px}
  .site-tagline{font-family:"Alice",Georgia,serif;font-size:19px;color:#333;margin-top:2px}

  .hero{position:absolute;left:0;top:110px;width:1200px;height:370px;
    background:linear-gradient(180deg,var(--sky-top) 0%,var(--sky-mid) 55%,var(--sky-low) 100%)}
  .hero-skyline{position:absolute;left:0;bottom:0;width:1200px;height:220px;
    background:linear-gradient(180deg,rgba(20,20,50,.2),rgba(40,25,60,.95))}
  .polaroid{position:absolute;background:#fff;padding:8px;box-shadow:0 4px 12px rgba(0,0,0,.5)}
  .polaroid .shot{width:100%;height:100%}
  .p1{left:330px;top:20px;width:150px;height:150px}
  .p2{left:490px;top:10px;width:110px;height:130px}
  .p3{left:230px;top:170px;width:140px;height:140px}
  .p4{left:410px;top:160px;width:170px;height:190px}
  .p5{left:600px;top:130px;width:110px;height:120px}
  .tone-a{background:linear-gradient(160deg,#f2c9a2,#b06c4a)}
  .tone-b{background:linear-gradient(160deg,#f5d6b8,#c78358)}
  .tone-c{background:linear-gradient(160deg,#e9c3a0,#7a4c3a)}
  .tone-d{background:linear-gradient(160deg,#f3dcc4,#9a6a50)}
  .tone-e{background:linear-gradient(160deg,#d9b08a,#5a3a2e)}

  .success-title{position:absolute;left:0;top:500px;width:1200px;text-align:center;
    font-family:"Alice",Georgia,serif;font-size:34px;color:#222;font-weight:400}
  .success-title em{font-style:normal;color:var(--teal)}

  .intro-video{position:absolute;left:200px;top:565px;width:360px;height:205px;
    background:linear-gradient(135deg,#8a6a5a,#3c2e3a 60%,#6a4e64)}
  .play-icon{position:absolute;left:50%;top:50%;transform:translate(-50%,-50%)}
  .intro-copy{position:absolute;left:200px;top:785px;width:360px;font-size:13px;line-height:1.5;color:#333}
  .intro-copy h3{font-size:14px;font-weight:700;color:#111;margin-bottom:6px}
  .intro-copy p{margin-bottom:10px}

  .lead-form{position:absolute;left:590px;top:560px;width:410px;height:470px;
    background:var(--teal-dark);padding:18px 24px;color:#fff}
  .lead-form h4{font-size:14px;font-weight:700;color:#bff2fa;line-height:1.3;width:330px}
  .lead-form .form-note{font-size:11.5px;line-height:1.4;margin-top:5px;color:#e4f8fb;width:320px}
  .lead-form .arrow-badge{position:absolute;right:22px;top:78px}
  .required-bar{margin-top:10px;background:var(--teal-deep);font-size:11px;padding:4px 8px;width:220px}
  .field{display:block;width:220px;height:26px;margin-top:6px;background:#fff;border:1px solid #bbb;
    font-size:12px;color:#777;padding:4px 8px;position:relative}
  .field.select::after{content:"";position:absolute;right:8px;top:10px;border:5px solid transparent;border-top-color:#555}
  .submit{display:block;margin-top:12px;width:220px;height:38px;background:var(--orange);
    border:1px solid var(--orange-dark);color:#fff;font-size:16px;font-weight:700;text-align:center;line-height:36px;border-radius:3px}

  .projects-band{position:absolute;left:0;top:1040px;width:1200px;height:1480px;background:var(--band)}
  .project-card{position:absolute;left:200px;width:800px;height:440px;background:var(--card);
    border:1px solid #c8c8c8}
  .card-1{top:30px}.card-2{top:500px}.card-3{top:970px}
  .card-photo{position:absolute;left:20px;top:20px;width:140px;height:230px;background:#fff;padding:6px;
    box-shadow:0 2px 6px rgba(0,0,0,.3)}
  .card-photo .shot{width:100%;height:100%}
  .recent{position:absolute;left:20px;top:270px;width:150px;font-size:14px}
  .recent h5{font-size:14px;font-weight:600;color:#333;margin-bottom:4px}
  .recent li{list-style:none;font-size:12px;color:#666;line-height:1.5}
  .recent li::before{content:"\203A  ";color:var(--teal)}
  .card-video{position:absolute;left:185px;top:20px;width:595px;height:300px}
  .v1{background:linear-gradient(135deg,#e87ab0,#6a3a8a 55%,#2a8ac8)}
  .v2{background:linear-gradient(135deg,#f0b040,#c84a6a 55%,#4a2a7a)}
  .v3{background:linear-gradient(135deg,#7ad0e8,#f2c26a 55%,#e06a4a)}
  .card-text{position:absolute;left:185px;top:335px;width:595px;font-size:11.5px;line-height:1.55;color:#555}

  .site-footer{position:absolute;left:0;top:2520px;width:1200px;height:48px;background:var(--footer);
    color:#ddd;font-size:13px;text-align:center;line-height:48px}
  .site-footer span{color:var(--teal)}
</style>
</head>
<body>

<header class="site-header">
  <h1 class="site-title">Bayline Talent Auditions</h1>
  <p class="site-tagline">Get Started in TV Commercials, Movies, Magazines &amp; More!</p>
</header>

<section class="hero" role="img" aria-label="New York City skyline at night with a collage of young actors' photos">
  <div class="hero-skyline"></div>
  <div class="polaroid p1"><div class="shot tone-a" role="img" aria-label="Portrait of a young actress"></div></div>
  <div class="polaroid p2"><div class="shot tone-b" role="img" aria-label="Portrait of a young actor"></div></div>
  <div class="polaroid p3"><div class="shot tone-c" role="img" aria-label="Portrait of a child performer"></div></div>
  <div class="polaroid p4"><div class="shot tone-d" role="img" aria-label="Portrait of a teen actress"></div></div>
  <div class="polaroid p5"><div class="shot tone-e" role="img" aria-label="Portrait of a teen actor"></div></div>
</section>

<h2 class="success-title">You could be our next <em>Success Story!</em></h2>

<div class="intro-video" role="img" aria-label="Video still of a group of young cast members">
  <svg class="play-icon" width="56" height="56" viewBox="0 0 56 56"><circle cx="28" cy="28" r="26" fill="rgba(0,0,0,.35)" stroke="#fff" stroke-width="3"/><path d="M22 17 L39 28 L22 39 Z" fill="#fff"/></svg>
</div>

<div class="intro-copy">
  <h3>Get Started in TV Commercials, Movies, Magazines &amp; More!</h3>
  <p>Enter today for your chance to be on a show like Marnie, Quiet clever sisters, The Spooky Pembertons and more! We are pre-screening for Hollywood's top Agents and Casting Directors. One lucky winner will win an all expense paid trip to New York City to meet hundreds of top agents, casting directors and managers.</p>
  <p>Ages 4 - 30 yrs only</p>
  <p>Auditions are being held in the Long Island Area!</p>
</div>

<form class="lead-form">
  <h4>Have you ever thought about being on TV or in Magazines?</h4>
  <p class="form-note">Fill out the form now for your chance to get started today! You will be contacted for the next available audition you are qualified for.</p>
  <svg class="arrow-badge" width="26" height="26" viewBox="0 0 26 26"><circle cx="13" cy="13" r="12" fill="#0a3e46"/><path d="M8 11 L13 17 L18 11" stroke="#fff" stroke-width="2.5" fill="none"/></svg>
  <div class="required-bar">* is required field</div>
  <span class="field">First Name *</span>
  <span class="field">Last Name *</span>
  <span class="field">Phone *</span>
  <span class="field">Email *</span>
  <span class="field">City</span>
  <span class="field select">Gender</span>
  <span class="field select">Age</span>
  <span class="field select">How did you hear about us?</span>
  <div class="submit">Get Started Now!</div>
</form>

<section class="projects-band">
  <article class="project-card card-1">
    <div class="card-photo"><div class="shot tone-b" role="img" aria-label="Full-length photo of a young actress"></div></div>
    <div class="recent"><h5>Recent Projects:</h5><ul><li>Gearshifters</li><li>Under Roman Skies</li></ul></div>
    <div class="card-video v1" role="img" aria-label="Video still from a family TV show">
      <svg class="play-icon" width="64" height="64" viewBox="0 0 56 56"><circle cx="28" cy="28" r="26" fill="rgba(0,0,0,.35)" stroke="#fff" stroke-width="3"/><path d="M22 17 L39 28 L22 39 Z" fill="#fff"/></svg>
    </div>
    <p class="card-text">Trent Vasquell (born March 3, 1978) is an American actor and former fashion model. He began his career in print ads before landing roles on network television, then moved into feature films. He has since starred in several popular family series and blockbuster movies, and he continues to mentor young performers across the country today.</p>
  </article>

  <article class="project-card card-2">
    <div class="card-photo"><div class="shot tone-a" role="img" aria-label="Portrait of a young actor"></div></div>
    <div class="recent"><h5>Recent Projects:</h5><ul><li>Gearshifters</li><li>Under Roman Skies</li></ul></div>
    <div class="card-video v2" role="img" aria-label="Video still from a teen comedy series">
      <svg class="play-icon" width="64" height="64" viewBox="0 0 56 56"><circle cx="28" cy="28" r="26" fill="rgba(0,0,0,.35)" stroke="#fff" stroke-width="3"/><path d="M22 17 L39 28 L22 39 Z" fill="#fff"/></svg>
    </div>
    <p class="card-text">Trent Vasquell (born March 3, 1978) is an American actor and former fashion model. He began his career in print ads before landing roles on network television, then moved into feature films. He has since starred in several popular family series and blockbuster movies, and he continues to mentor young performers across the country today.</p>
  </article>

  <article class="project-card card-3">
    <div class="card-photo"><div class="shot tone-c" role="img" aria-label="Portrait of a young actress"></div></div>
    <div class="recent"><h5>Recent Projects:</h5><ul><li>Gearshifters</li><li>Under Roman Skies</li></ul></div>
    <div class="card-video v3" role="img" aria-label="Video still from a beach musical movie">
      <svg class="play-icon" width="64" height="64" viewBox="0 0 56 56"><circle cx="28" cy="28" r="26" fill="rgba(0,0,0,.35)" stroke="#fff" stroke-width="3"/><path d="M22 17 L39 28 L22 39 Z" fill="#fff"/></svg>
    </div>
    <p class="card-text">Trent Vasquell (born March 3, 1978) is an American actor and former fashion model. He began his career in print ads before landing roles on network television, then moved into feature films. He has since starred in several popular family series and blockbuster movies, and he continues to mentor young performers across the country today.</p>
  </article>
</section>

<footer class="site-footer"><span>Click here</span> to Read our Privacy Policy</footer>

</body>
</html>
```